B2B flyer solution for charging infrastructures (One-Pager Din A4, double-sided)

We need a professional design for our flyer in format Din A4/both sides.
Attached you will find the content for the flyer, but we are looking for a modern, professional design.

Some background/context information:
- the product is about a solution for charging and billing of charging infrastructures (for electric cars) in companies
- target group: companies, esp. facility managers, fleet managers, controlling, CTO, CEO
- should be printed and available online
- our website (and most of our current design work): https://wendo-kraft.de

In the files you will find:
- photos of reference implementations of our solution (should be included in the flyer)
- stock photos (we are using the one you will find in the current flyer on our presentations, maybe you can use it too to keep some corporate identity.
- our logo
- the current flyer as PDF and as PowerPoint
- a sample presentation we also need for customer communication

It would be nice if the design will align with the existing design work, but bring fresh aspects and will be up-to-date and professional.

Target Market(s)

B2B, companies, fleet managers, facility managers, CTO, CIO

Industry/Entity Type

Enterprises, Charging Solutions for Electric Vehicles

Requirements
Nice to have
• Bright, light design, clean, readable

```html
<!DOCTYPE html>
<html lang="de">
<head>
<meta charset="utf-8">
<title>wendo-kraft Professional – Flyer</title>
<link href="https://fonts.googleapis.com/css2?family=Source+Sans+3:wght@400;600;700&display=swap" rel="stylesheet">
<style>
:root{
  --magenta:#d22f8f;
  --purple:#7a4ec8;
  --violet:#8d62d8;
  --panel:#dde6f8;
  --ink:#1b1b2b;
  --stage:#cfcfcf;
  --paper:#ffffff;
  --band:linear-gradient(90deg,#7a4ec8 0%,#b53fae 55%,#d22f8f 100%);
}
*{box-sizing:border-box;margin:0;padding:0}
html,body{width:1200px;height:1177px;overflow:hidden}
body{background:var(--stage);font-family:"Source Sans 3",Arial,sans-serif;color:var(--ink);position:relative}
.page{position:absolute;top:215px;width:528px;height:745px;background:var(--paper);overflow:hidden}
.page--front{left:58px}
.page--back{left:618px}
.abs{position:absolute}
.nowrap{white-space:nowrap}
.brand{display:flex;align-items:center;gap:8px;font-size:21px;font-weight:600;color:var(--ink);white-space:nowrap}
.brand__mark{width:14px;height:14px;background:var(--magenta)}
.title{font-size:22px;font-weight:700;line-height:1;white-space:nowrap}
.title .a{color:var(--magenta)} .title .b{color:var(--violet)}
.subtitle{font-size:11.5px;font-weight:700;white-space:nowrap}
.lead{font-size:11px;line-height:15px;white-space:nowrap}
.lead strong{font-size:12px}
.panel{background:var(--panel)}
.pill{background:var(--band);color:#fff;font-weight:700;border-radius:12px;display:flex;align-items:center;justify-content:center;white-space:nowrap}
.pill--spaced{letter-spacing:5px;font-size:13.5px}
.pill--section{font-size:10.5px;border-radius:10px}
.service{position:absolute;left:262px;display:flex;gap:8px;font-size:10px;line-height:12.5px;white-space:nowrap}
.service__icon{flex:none;width:20px;height:20px;border-radius:50%;background:var(--violet)}
.checks{list-style:none;font-size:9.5px;line-height:14px;white-space:nowrap}
.checks li::before{content:"✓";color:var(--magenta);font-weight:700;margin-right:6px}
.contact{font-size:11px;line-height:13px;white-space:nowrap}
.contact b{color:var(--magenta)}
.band{left:14px;width:496px;top:691px;height:30px;border-radius:15px;background:var(--band);display:flex;align-items:center;justify-content:space-around;color:#fff;font-size:12px;font-weight:700;white-space:nowrap}
.band__item{display:flex;align-items:center;gap:7px}
.band__dot{width:20px;height:20px;border-radius:50%;background:#fff;display:flex;align-items:center;justify-content:center}
.tagline{top:731px;width:100%;text-align:center;font-size:9.5px}
.copy{font-size:10px;line-height:12px;white-space:nowrap}
.bullets{list-style:none;font-weight:700;font-size:9.8px;line-height:11.7px;margin-top:4px;white-space:nowrap}
.bullets li{padding-left:10px;position:relative}
.bullets li::before{content:"";position:absolute;left:0;top:4px;width:5px;height:5px;border-radius:50%;background:var(--magenta)}
.sidebar-title{font-size:14px;font-weight:600;text-align:center;line-height:17px;width:164px}
.tile{left:372px;width:110px;height:71px;border:1.5px solid var(--magenta);border-radius:8px;background:#fff;display:flex;flex-direction:column;align-items:center;justify-content:flex-end;padding-bottom:6px;font-size:9.5px;text-align:center;line-height:1.15}
.tile svg{margin-bottom:4px}
</style>
</head>
<body>

<!-- FRONT -->
<section class="page page--front">
  <svg class="abs" style="left:17px;top:14px" width="494" height="209" role="img" aria-label="Foto: Ladestecker an einem Elektroauto mit blau leuchtendem Ladeanschluss">
    <defs><linearGradient id="heroBlue" x1="0" y1="0" x2="1" y2="1"><stop offset="0" stop-color="#cfd9ef"/><stop offset=".5" stop-color="#4c7fd9"/><stop offset="1" stop-color="#1d3fa6"/></linearGradient></defs>
    <path d="M183 14 Q183 0 197 0 H480 Q494 0 494 14 V209 H0 V145 Q0 131 14 131 H169 Q183 131 183 117 Z" fill="url(#heroBlue)"/>
  </svg>
  <div class="abs brand" style="left:17px;top:66px"><span class="brand__mark"></span>wendo-kraft.de</div>

  <div class="abs title" style="left:19px;top:233px"><span class="a">wendo-kraft</span> <span class="b">Professional</span></div>
  <div class="abs subtitle" style="left:19px;top:258px">die maßgeschneiderte B2B-Abrechnungslösung für Elektromobilität</div>
  <p class="abs lead" style="left:19px;top:287px">Lade-Infrastruktur-Abrechnungslösungen für Unternehmen,<br>damit Lade-Infrastruktur Erträge statt Kosten produziert.<br><strong>So wird Lade-Infrastruktur von einer Kostenstelle zu einem Profitcenter.</strong></p>

  <div class="abs panel" style="left:242px;top:385px;width:270px;height:306px"></div>
  <div class="abs" role="img" aria-label="Foto: Wandladestation mit grünem Ladekabel in einer Tiefgarage" style="left:17px;top:353px;width:225px;height:230px;background:linear-gradient(135deg,#8d8a86,#4e4c4a 60%,#2f2e2d)"></div>

  <div class="abs pill pill--spaced" style="left:296px;top:371px;width:170px;height:24px">Leistungen</div>
  <div class="service" style="top:410px"><span class="service__icon"></span><span>Vielseitige Abrechnungsmöglichkeiten für<br>Fuhrpark, Mitarbeiter, Partnerunternehmen,<br>Mieter, Kunden und andere.</span></div>
  <div class="service" style="top:466px"><span class="service__icon"></span><span>Full-Service-Betreuung<br>(Monitoring, Abrechnung, Benutzerbetreuung)</span></div>
  <div class="service" style="top:503px"><span class="service__icon"></span><span style="padding-top:4px">Integration in ihre Unternehmensabläufe</span></div>
  <div class="service" style="top:530px"><span class="service__icon"></span><span>Berücksichtigung von Eigentümer/<br>Mieter-Konstellationen</span></div>

  <div class="abs pill" style="left:257px;top:577px;width:250px;height:24px;font-size:11.5px">Mit wendo-kraft Professional profitieren</div>
  <ul class="abs checks" style="left:256px;top:618px">
    <li>Effizienter Verwaltung von Lade-Infrastruktur</li>
    <li>Umfassende Full-Service-Betreuung</li>
    <li>Nahtloser Integration in Ihre kaufmännischen Prozesse</li>
    <li>Vielseitigen Abrechnungsmöglichkeiten</li>
  </ul>
  <p class="abs contact" style="left:26px;top:608px"><b>Kontaktieren</b> Sie uns um Erfahren<br>Sie mehr über wendo-kraft und wie<br>wir Ihre Abrechnungsanforderungen<br>erfüllen können. Kontaktieren<br>Sie uns für eine kostenlose Beratung:</p>

  <div class="abs band">
    <span class="band__item"><span class="band__dot"><svg width="11" height="11" viewBox="0 0 24 24"><path d="M6.6 10.8a15 15 0 0 0 6.6 6.6l2.2-2.2a1 1 0 0 1 1-.25 11 11 0 0 0 3.6.6 1 1 0 0 1 1 1V20a1 1 0 0 1-1 1A17 17 0 0 1 3 4a1 1 0 0 1 1-1h3.5a1 1 0 0 1 1 1 11 11 0 0 0 .6 3.6 1 1 0 0 1-.25 1z" fill="#7a4ec8"/></svg></span>+49 (0) 9876 543 210</span>
    <span class="band__item"><span class="band__dot"><svg width="11" height="9" viewBox="0 0 22 16"><rect x="1" y="1" width="20" height="14" rx="2" fill="#b53fae"/><path d="M1 2l10 7 10-7" stroke="#fff" stroke-width="1.6" fill="none"/></svg></span>info@wendo-kraft.de</span>
    <span class="band__item"><span class="band__dot"><svg width="12" height="12" viewBox="0 0 24 24"><circle cx="12" cy="12" r="10" fill="none" stroke="#d22f8f" stroke-width="2"/><path d="M2 12h20M12 2c3 3 3 17 0 20M12 2c-3 3-3 17 0 20" fill="none" stroke="#d22f8f" stroke-width="1.6"/></svg></span>www.wendo-kraft.de</span>
  </div>
  <div class="abs tagline">wendo-kraft - Die Abrechnungslösung für Lade-Infrastruktur in Unternehmen.</div>
</section>

<!-- BACK -->
<section class="page page--back">
  <svg class="abs" style="left:16px;top:11px" width="490" height="189" role="img" aria-label="Foto: blauer Ladestecker an einer Ladesäule vor unscharfen Lichtern">
    <defs><linearGradient id="plugBlue" x1="0" y1="0" x2="1" y2="0"><stop offset="0" stop-color="#2c2f3a"/><stop offset=".45" stop-color="#3b5fb8"/><stop offset="1" stop-color="#c9c3cf"/></linearGradient></defs>
    <path d="M0 14 Q0 0 14 0 H246 Q260 0 260 14 V82 Q260 96 274 96 H476 Q490 96 490 110 V189 H0 Z" fill="url(#plugBlue)"/>
  </svg>
  <div class="abs brand" style="right:24px;top:66px"><span class="brand__mark"></span>wendo-kraft.de</div>

  <div class="abs panel" style="left:345px;top:200px;width:162px;height:491px"></div>
  <div class="abs sidebar-title" style="left:345px;top:222px">Verrechnung von<br>Ladevorgängen für:</div>

  <div class="abs tile" style="top:256px">
    <svg width="80" height="22" viewBox="0 0 80 22"><g fill="#1b1b2b"><path d="M2 16v-5l4-6h12l4 6v5z"/><path d="M29 16v-5l4-6h12l4 6v5z"/><path d="M56 16v-5l4-6h12l4 6v5z"/><circle cx="7" cy="18" r="3"/><circle cx="17" cy="18" r="3"/><circle cx="34" cy="18" r="3"/><circle cx="44" cy="18" r="3"/><circle cx="61" cy="18" r="3"/><circle cx="71" cy="18" r="3"/></g></svg>
    Fuhrpark,<br>Dienstwagen</div>
  <div class="abs tile" style="top:334px">
    <svg width="44" height="24" viewBox="0 0 44 24"><g fill="#1b1b2b"><circle cx="10" cy="7" r="4.5"/><circle cx="22" cy="6" r="5"/><circle cx="34" cy="7" r="4.5"/><path d="M2 22a8 8 0 0 1 16 0zM13 22a9 9 0 0 1 18 0zM26 22a8 8 0 0 1 16 0z"/></g></svg>
    Mitarbeiter<br>Privatfahrzeuge</div>
  <div class="abs tile" style="top:412px">
    <svg width="30" height="30" viewBox="0 0 30 30"><g fill="#1b1b2b"><circle cx="15" cy="4" r="3"/><circle cx="8" cy="10" r="3"/><circle cx="22" cy="10" r="3"/><circle cx="15" cy="16" r="3"/><path d="M3 28a5 5 0 0 1 10 0zM10 22a5 5 0 0 1 10 0zM17 28a5 5 0 0 1 10 0z"/></g></svg>
    Kunden<br>und Gäste</div>
  <div class="abs tile" style="top:490px">
    <svg width="34" height="28" viewBox="0 0 34 28"><g fill="#1b1b2b"><rect x="2" y="10" width="9" height="18"/><rect x="12" y="2" width="10" height="26"/><rect x="23" y="8" width="9" height="20"/></g></svg>
    Vermieter,<br>Eigentümer</div>
  <div class="abs" role="img" aria-label="Foto: Reihe von Ladesäulen mit grünen Kabeln vor einer Hecke" style="left:355px;top:574px;width:142px;height:106px;background:linear-gradient(120deg,#6e7a4e,#a8a89c 55%,#d8d6d0)"></div>

  <div class="abs title" style="left:26px;top:216px"><span class="a">wendo-kraft</span> <span class="b">Professional</span></div>
  <div class="abs subtitle" style="left:26px;top:239px">die Funktionen im Überblick</div>

  <div class="abs pill pill--section" style="left:26px;top:268px;width:300px;height:20px">Full-Service-Betreuung für sorgenfreies Management</div>
  <div class="abs" style="left:32px;top:297px">
    <p class="copy">wendo-kraft übernimmt auf Wunsch alle organisatorischen Belange<br>bei der Verwaltung Ihrer Lade-Infrastruktur, einschließlich:</p>
    <ul class="bullets"><li>Monitoring</li><li>Support</li><li>User-Onboarding und -Support</li><li>Handling von Zugangskarten</li><li>Integration von firmeninternen Zugangstoken</li></ul>
  </div>

  <div class="abs pill pill--section" style="left:26px;top:399px;width:300px;height:20px">Perfekte Integration in kaufmännische Prozesse</div>
  <div class="abs" style="left:32px;top:428px">
    <p class="copy">wendo-kraft fügt sich nahtlos in die kaufmännischen Strukturen<br>moderner Unternehmen ein und bietet:</p>
    <ul class="bullets"><li>Erweitertes Reporting</li><li>Aufschlüsselung und Tarifierung nach Nutzergruppe</li><li>Unterstützung unternehmensinterner Abrechnung und</li><li>Verrechnung und/oder Zahlungseinzug durch wendo-kraft</li><li>Schnittstellen zu Buchhaltung und Lohnbuchhaltung</li><li>Bedarfsgerechte Anpassbarkeit</li></ul>
  </div>

  <div class="abs pill pill--section" style="left:26px;top:540px;width:300px;height:20px">Besonderer Aspekt: Eigentümer-Mieter-Konstellationen</div>
  <div class="abs" style="left:32px;top:569px">
    <p class="copy">Häufige Situation: Der Mieter eines Objektes benötigt Lade-<br>Infrastruktur, der Eigentümer/Verwalter möchte nicht zusätzlich<br>belastet werden.</p>
    <ul class="bullets"><li>Unterschiedliche Betreibermodelle für verschiedene<br>Situationen (Langzeit-Mieter vs. Kurzzeit-Mieter)</li><li>Kauf-, Miet- und Leasing-Optionen</li><li>Kostenneutral für Eigentümer/Verwalter durch geeignete<br>Abrechnungsmodelle</li></ul>
  </div>

  <div class="abs band">
    <span class="band__item"><span class="band__dot"><svg width="11" height="11" viewBox="0 0 24 24"><path d="M6.6 10.8a15 15 0 0 0 6.6 6.6l2.2-2.2a1 1 0 0 1 1-.25 11 11 0 0 0 3.6.6 1 1 0 0 1 1 1V20a1 1 0 0 1-1 1A17 17 0 0 1 3 4a1 1 0 0 1 1-1h3.5a1 1 0 0 1 1 1 11 11 0 0 0 .6 3.6 1 1 0 0 1-.25 1z" fill="#7a4ec8"/></svg></span>+49 (0) 9876 543 210</span>
    <span class="band__item"><span class="band__dot"><svg width="11" height="9" viewBox="0 0 22 16"><rect x="1" y="1" width="20" height="14" rx="2" fill="#b53fae"/><path d="M1 2l10 7 10-7" stroke="#fff" stroke-width="1.6" fill="none"/></svg></span>info@wendo-kraft.de</span>
    <span class="band__item"><span class="band__dot"><svg width="12" height="12" viewBox="0 0 24 24"><circle cx="12" cy="12" r="10" fill="none" stroke="#d22f8f" stroke-width="2"/><path d="M2 12h20M12 2c3 3 3 17 0 20M12 2c-3 3-3 17 0 20" fill="none" stroke="#d22f8f" stroke-width="1.6"/></svg></span>www.wendo-kraft.de</span>
  </div>
  <div class="abs tagline">wendo-kraft - Die Abrechnungslösung für Lade-Infrastruktur in Unternehmen.</div>
</section>

</body>
</html>
```